Microblading website contest - Make it colorful

Beauty salon focusing on microblading need a better website template. Please make a 1 page site mobile optimized and nicer layout with better color formulation. Would love interactive images in the site. You can use stock images and if approve we can pay for it.
Current site:
tessawynkelpeony.com

Inspiration:
https://framqueue.net/shots/41877260-Microblading-HomePage
https://framqueue.net/shots/7914026-Lunetto-Microblading-Eyebrow-Beauty-Salon-Pagewright-Theme

Target Market(s)

women

Industry/Entity Type

beauty salon

Number of Pages Required

1 page

Font styles to use
Serif
Decorative
Script

Requirements
Nice to have
• As pretty as possible

```html
<!DOCTYPE html>
<html lang="en">
<head>
<meta charset="utf-8">
<title>Atelier Marela Brows — Microblading</title>
<link href="https://fonts.googleapis.com/css2?family=PT+Serif:wght@400;700&family=Montserrat:wght@400;500;600&family=Great+Vibes&display=swap" rel="stylesheet">
<style>
:root{
  --rose:#d13f64;
  --rose-soft:#f4cbd6;
  --blush:#f8eeec;
  --page:#f5f4f4;
  --ink:#222;
  --muted:#555;
  --night:#1a1a1a;
  --white:#fff;
}
*{margin:0;padding:0;box-sizing:border-box}
html,body{width:1200px;height:4164px;overflow:hidden}
body{position:relative;background:var(--page);font-family:"Montserrat",Arial,sans-serif;color:var(--ink)}
.abs{position:absolute}
.serif{font-family:"PT Serif",Georgia,serif}
.btn{position:absolute;display:flex;align-items:center;justify-content:center;gap:14px;font-family:"PT Serif",Georgia,serif;font-size:12px;letter-spacing:1.5px;text-transform:uppercase}
.btn-rose{background:var(--rose);color:var(--white)}
.btn-rose::before{content:"";width:26px;height:1px;background:currentColor}
.btn-line{border:1.5px solid #555;color:#333;background:transparent}
.center{text-align:center;left:0;width:1200px}
.section-title{font-family:"PT Serif",Georgia,serif;font-size:46px;font-weight:400;color:var(--ink)}
.lede{font-size:14px;line-height:19px;color:#333}
.sprig{position:absolute;border-radius:50%;background:radial-gradient(closest-side,rgba(236,214,196,.75),rgba(226,214,228,.35) 60%,rgba(245,244,244,0))}

/* hero */
.hero{left:0;top:0;width:1200px;height:676px;background:
  radial-gradient(ellipse 360px 420px at 900px 230px,rgba(176,150,140,.55),rgba(0,0,0,0) 70%),
  radial-gradient(ellipse 420px 300px at 230px 470px,rgba(40,34,36,.7),rgba(0,0,0,0) 75%),
  linear-gradient(100deg,#4a4345 0%,#6b6264 40%,#8a7f7d 62%,#5c5354 82%,#3e3739 100%)}
.nav a{position:absolute;top:36px;color:var(--white);font-size:12px;letter-spacing:.4px;text-decoration:none}
.brand{left:113px;top:28px;color:var(--white);font-family:"PT Serif",Georgia,serif;font-size:20px}
.welcome{top:148px;font-family:"Great Vibes",cursive;font-size:28px;color:#e0557a}
.hero-rule{top:167px;height:1px;width:140px;background:var(--rose)}
.hero-title{top:196px;font-family:"PT Serif",Georgia,serif;font-size:66px;color:var(--white)}
.hero-sub{top:288px;font-size:22px;color:var(--white)}

/* features */
.features{left:113px;top:556px;width:974px;height:359px;background:var(--white)}
.feature-back{position:absolute;top:0;width:200px;height:336px;background:var(--rose-soft)}
.feature{position:absolute;top:18px;width:194px;height:301px;background:var(--rose);color:var(--white)}
.feature h3{position:absolute;left:21px;top:98px;font-family:"PT Serif",Georgia,serif;font-weight:400;font-size:22px;line-height:26px}
.feature p{position:absolute;left:21px;top:200px;width:150px;font-size:11px;line-height:18px}
.feature .more{position:absolute;left:0;bottom:0;width:194px;height:37px;background:var(--night);display:flex;align-items:center;justify-content:center;gap:14px;font-family:"PT Serif",Georgia,serif;font-size:12px;letter-spacing:1.5px}
.feature .more::before{content:"";width:26px;height:1px;background:var(--white)}

/* services */
.service{position:absolute;top:1887px;width:223px;height:293px}
.service span{position:absolute;left:18px;bottom:20px;color:var(--white);font-family:"PT Serif",Georgia,serif;font-size:22px}
.arrow{position:absolute;width:48px;height:48px;border-radius:50%;display:flex;align-items:center;justify-content:center}
.arrow.prev{background:#efc4cf}
.arrow.next{background:var(--rose)}

/* specialized */
.special-item h4{font-family:"PT Serif",Georgia,serif;font-weight:400;font-size:15px;color:#333}
.special-item p{font-size:11px;line-height:19px;color:#555}
.special-note{font-size:10px;line-height:16px;color:#555;text-align:right}

/* blog */
.blog-img{position:absolute;top:3150px;width:303px;height:207px}
.blog-card{position:absolute;top:3328px;width:257px;height:107px;background:var(--white);text-align:center}
.blog-card .date{margin-top:21px;font-size:11px;color:#444}
.blog-card h5{margin-top:6px;font-family:"PT Serif",Georgia,serif;font-weight:400;font-size:16px;color:#333}
.blog-card .link{margin-top:12px;display:flex;justify-content:center;align-items:center;gap:12px;font-family:"PT Serif",Georgia,serif;font-size:12px;letter-spacing:1.5px}
.blog-card .link::before{content:"";width:26px;height:1px;background:currentColor}
.blog-card.active{background:var(--rose);color:var(--white);outline:1px solid var(--white);outline-offset:-6px}
.blog-card.active .date,.blog-card.active h5{color:var(--white)}

/* footer */
.footer{left:0;top:3836px;width:1200px;height:328px;background:var(--night);color:var(--white)}
.footer h6{position:absolute;top:44px;font-family:"PT Serif",Georgia,serif;font-weight:400;font-size:15px}
.footer li{list-style:none;font-size:10.5px;height:31.5px}
.contact-row{position:absolute;display:flex;align-items:center;gap:12px;font-size:10.5px}
</style>
</head>
<body>

<!-- hero -->
<div class="abs hero" role="img" aria-label="Photo of a masked brow artist working closely on a client's eyebrows"></div>
<div class="abs brand">Microblading</div>
<nav class="nav">
  <a style="left:320px">HOME</a>
  <span class="abs" style="left:329px;top:58px;width:20px;height:2px;background:var(--rose)"></span>
  <a style="left:388px">ABOUT</a>
  <a style="left:458px">SERVICES</a>
  <a style="left:545px">GALLERY</a>
  <a style="left:626px">SHOP</a>
  <a style="left:688px">ACADEMY</a>
  <a style="left:776px">TESTIMONIAL</a>
  <a style="left:884px">CONTACT US</a>
</nav>
<svg class="abs" style="left:1005px;top:26px" width="24" height="28" viewBox="0 0 24 28" fill="none" stroke="#fff" stroke-width="1.6"><circle cx="12" cy="8" r="6"/><path d="M2 27c0-6 4-10 10-10s10 4 10 10"/></svg>
<svg class="abs" style="left:1050px;top:30px" width="28" height="26" viewBox="0 0 28 26" fill="none" stroke="#fff" stroke-width="1.6"><path d="M1 2h4l4 15h14l3-10H7"/><circle cx="11" cy="22" r="2"/><circle cx="21" cy="22" r="2"/></svg>
<div class="abs" style="left:1070px;top:21px;width:16px;height:16px;border-radius:50%;background:var(--rose);color:#fff;font-size:9px;display:flex;align-items:center;justify-content:center">1</div>

<div class="abs hero-rule" style="left:308px"></div>
<div class="abs hero-rule" style="left:752px"></div>
<div class="abs center welcome">Welcome to Microblading</div>
<div class="abs center hero-title">Atelier Marela Brows</div>
<div class="abs center hero-sub">&gt;&gt;&gt; Your personal eyebrow specialist</div>
<div class="btn btn-rose" style="left:511px;top:354px;width:178px;height:38px">Book now</div>

<!-- features -->
<section class="abs features">
  <div class="abs" style="left:0;top:0;width:290px;height:359px;background:linear-gradient(160deg,#fff 50%,#f5f0ef 100%)"></div>
  <h2 class="abs serif" style="left:45px;top:22px;font-weight:400;font-size:44px;line-height:50px;color:var(--ink)">Your<br>Eyebrows<br>and<br>Beauty</h2>
  <span class="abs" style="left:155px;top:53px;width:56px;height:1px;background:#333"></span>
  <p class="abs" style="left:43px;top:248px;font-size:13px;color:#333">Let us take care of it</p>
  <div class="abs" style="left:45px;top:306px;display:flex;align-items:center;gap:14px;font-family:'PT Serif',Georgia,serif;font-size:12px;letter-spacing:1.4px"><span style="width:28px;height:1px;background:#333"></span>SHOW MORE</div>

  <div class="feature-back" style="left:285px"></div>
  <div class="feature-back" style="left:523px"></div>
  <div class="feature-back" style="left:761px"></div>

  <div class="feature" style="left:304px">
    <svg class="abs" style="left:21px;top:20px" width="56" height="56" viewBox="0 0 56 56" fill="none" stroke="#fff" stroke-width="1.4"><circle cx="28" cy="28" r="26" fill="#fff" fill-opacity=".15" stroke="none"/><rect x="18" y="14" width="20" height="26" rx="2"/><path d="M22 21h12M22 26h12M22 31h8"/><circle cx="36" cy="38" r="5"/></svg>
    <h3>Licensed<br>microblading<br>artist</h3>
    <p>License from various states in United State</p>
    <div class="more">LEARN MORE</div>
  </div>
  <div class="feature" style="left:542px">
    <div class="abs" style="left:6px;top:6px;width:182px;height:252px;border:1px solid rgba(255,255,255,.7)"></div>
    <svg class="abs" style="left:21px;top:20px" width="56" height="56" viewBox="0 0 56 56" fill="none" stroke="#fff" stroke-width="1.4"><circle cx="28" cy="28" r="26" fill="#fff" fill-opacity=".15" stroke="none"/><circle cx="28" cy="24" r="9"/><path d="M24 33v6h8v-6M28 8v4M14 24h-4M46 24h-4"/></svg>
    <h3>Years<br>of<br>experience</h3>
    <p>Over thousands of cases Oversea study and practice</p>
    <div class="more">LEARN MORE</div>
  </div>
  <div class="feature" style="left:780px">
    <svg class="abs" style="left:21px;top:20px" width="56" height="56" viewBox="0 0 56 56" fill="none" stroke="#fff" stroke-width="1.4"><circle cx="28" cy="28" r="26" fill="#fff" fill-opacity=".15" stroke="none"/><circle cx="28" cy="24" r="9"/><path d="M24 33v6h8v-6M28 8v4M14 24h-4M46 24h-4M18 14l3 3M38 14l-3 3"/></svg>
    <h3>European<br>latest<br>technique</h3>
    <p>We study European -style natural hair flow, improve...</p>
    <div class="more">LEARN MORE</div>
  </div>
</section>

<!-- about -->
<div class="sprig" role="img" aria-label="Leaf sprig decoration" style="left:-20px;top:940px;width:170px;height:200px"></div>
<div class="sprig" role="img" aria-label="Leaf sprig decoration" style="left:1000px;top:1020px;width:200px;height:240px"></div>
<h2 class="abs center section-title" style="top:968px">About Marela</h2>
<div class="abs lede" style="left:190px;top:1043px;width:820px;text-align:center">
  <p>Marela has 7 years of microblading experience. She graduated from LumaDerm United States. After, she studied in Velora Academy, a global top brand from Germany. She was personally guided by the brand CEO Anton Kessler and Dr Mei Laurent.</p>
  <p style="margin-top:18px">After earning award of VeloBrows Artist in 2019. Marela continued her practice microblading until she won the world's first VeloBrows Master in Taiwan in 2021. She is currently the only certificated Master technician in Taiwan. She also holds a shading and VeloGlow Master.</p>
</div>
<div class="btn btn-rose" style="left:511px;top:1209px;width:178px;height:38px">Learn more</div>

<!-- video -->
<div class="abs" role="img" aria-label="Video still of a microblading class with students practising at tables" style="left:113px;top:1298px;width:974px;height:405px;background:
  radial-gradient(ellipse 260px 200px at 280px 250px,rgba(196,160,168,.6),rgba(0,0,0,0) 75%),
  radial-gradient(ellipse 220px 160px at 680px 300px,rgba(60,40,50,.55),rgba(0,0,0,0) 75%),
  linear-gradient(180deg,#8d7d84 0%,#7a5e6a 45%,#5e3c4f 100%)"></div>
<div class="abs" style="left:135px;top:1318px;width:935px;height:365px;border:1px solid rgba(255,255,255,.6)"></div>
<svg class="abs" style="left:562px;top:1468px" width="76" height="76" viewBox="0 0 76 76"><circle cx="38" cy="38" r="38" fill="#d13f64"/><path d="M30 24l24 14-24 14z" fill="#fff"/></svg>

<!-- services -->
<div class="sprig" role="img" aria-label="Leaf sprig decoration" style="left:-30px;top:1740px;width:180px;height:160px"></div>
<div class="sprig" role="img" aria-label="Leaf sprig decoration" style="left:1040px;top:1720px;width:180px;height:170px"></div>
<h2 class="abs center section-title" style="top:1751px">Our Services</h2>
<p class="abs lede" style="left:320px;top:1815px;width:560px;text-align:center">Lorem ipsum dolor sit amet, consectetur adipiscing elit, sed do eiusmod tempor incididunt ut labore et dolore magna aliqua.</p>

<div class="service" style="left:113px;background:radial-gradient(ellipse 120px 60px at 130px 120px,rgba(120,80,60,.55),rgba(0,0,0,0) 80%),linear-gradient(180deg,#e7cfc0 0%,#d8b4a3 55%,#b46a76 85%,#9a3a57 100%)" role="img" aria-label="Close-up of a hair stroke eyebrow being drawn"><span>Hair Stroke</span></div>
<div class="service" style="left:363px;background:radial-gradient(ellipse 90px 120px at 110px 120px,rgba(226,180,160,.8),rgba(0,0,0,0) 80%),linear-gradient(180deg,#d9b6a0 0%,#e5c5b2 45%,#c9998a 80%,#b07a70 100%)" role="img" aria-label="Portrait of a woman with natural brows">
  <div class="abs" style="left:4px;top:4px;width:215px;height:285px;border:1px solid rgba(255,255,255,.8)"></div>
  <span style="bottom:78px">Natural Brows</span>
  <div class="btn btn-rose" style="left:20px;top:218px;width:178px;height:36px">Learn more</div>
</div>
<div class="service" style="left:613px;background:radial-gradient(ellipse 60px 110px at 140px 110px,rgba(70,50,45,.55),rgba(0,0,0,0) 80%),linear-gradient(180deg,#ead6cb 0%,#d9b9aa 55%,#b56a78 85%,#9a3a57 100%)" role="img" aria-label="Brow artist shaping powder brows on a client"><span>Powder Brows</span></div>
<div class="service" style="left:864px;background:radial-gradient(ellipse 100px 70px at 110px 130px,rgba(196,98,90,.55),rgba(0,0,0,0) 80%),linear-gradient(180deg,#c9a08e 0%,#b98476 50%,#a05a66 80%,#8e3553 100%)" role="img" aria-label="Close-up of an eye with makeup eyeliner"><span>Makeup Eyeliner</span></div>

<div class="arrow prev" style="left:31px;top:2010px"><svg width="14" height="14" viewBox="0 0 14 14"><path d="M9 2L4 7l5 5" stroke="#fff" stroke-width="2" fill="none"/></svg></div>
<div class="arrow next" style="left:1121px;top:2010px"><svg width="14" height="14" viewBox="0 0 14 14"><path d="M5 2l5 5-5 5" stroke="#fff" stroke-width="2" fill="none"/></svg></div>
<div class="btn btn-line" style="left:511px;top:2220px;width:178px;height:39px">View all</div>

<!-- specialized -->
<section class="abs" style="left:0;top:2307px;width:1200px;height:680px;background:var(--night)"></section>
<div class="abs" role="img" aria-label="Portrait of the brow artist smiling in a white top" style="left:113px;top:2358px;width:394px;height:577px;background:
  radial-gradient(ellipse 110px 140px at 200px 190px,rgba(226,196,180,.85),rgba(0,0,0,0) 80%),
  radial-gradient(ellipse 170px 240px at 230px 300px,rgba(40,30,30,.45),rgba(0,0,0,0) 80%),
  linear-gradient(180deg,#e9e9e9 0%,#dcdcdc 60%,#f2f2f2 100%)"></div>
<div class="abs" style="left:507px;top:2358px;width:580px;height:577px;background:linear-gradient(135deg,var(--blush) 0%,#f4e7e3 100%)"></div>
<h2 class="abs serif" style="left:561px;top:2396px;font-weight:400;font-size:44px;color:var(--ink)">Specialized service</h2>
<div class="abs" style="left:563px;top:2465px;width:440px;font-size:11px;line-height:19px;color:#555">
  <p>We treat every client as our friends and family. We give you the most sincere advise and best quality and service.</p>
  <p>We do not only follow the trend. We hear you, and want you to love it forever.</p>
</div>
<div class="abs" style="left:563px;top:2550px;width:450px;height:1px;background:#e2d3cf"></div>
<div class="abs special-item" style="left:563px;top:2563px"><h4>Natural Brows</h4><p style="margin-top:10px">Microblading | Hand-drawing hair lines</p></div>
<div class="abs special-note" style="left:850px;top:2563px;width:163px">For all skin type</div>
<div class="abs special-item" style="left:563px;top:2640px;width:290px"><h4>Powder Eyeliner (Natural Eyeshadow)</h4><p style="margin-top:8px">Extend eyeline at end of the eye| With a touch of ligh eyeshadow vision</p></div>
<div class="abs special-note" style="left:868px;top:2640px;width:145px">For those who like to have an eye makeup filter 24/7 | Eye-shape adjustment</div>
<div class="abs special-item" style="left:563px;top:2737px;width:290px"><h4>Scalp Micropigmentation</h4><p style="margin-top:8px">Add destiny to the thinning area | Seamless and Undetectable | Accommodates your skin tone and natural hair color | providing the appearance of hair</p></div>
<div class="abs special-note" style="left:868px;top:2737px;width:145px">For restoring hairline | Bald spots | Scar covering</div>
<div class="btn btn-rose" style="left:563px;top:2847px;width:178px;height:38px">Services</div>

<!-- blog -->
<div class="sprig" role="img" aria-label="Leaf sprig decoration" style="left:-30px;top:2980px;width:170px;height:150px"></div>
<div class="sprig" role="img" aria-label="Leaf sprig decoration" style="left:1060px;top:3390px;width:160px;height:200px"></div>
<h2 class="abs center section-title" style="top:3015px">Recent Blog</h2>
<p class="abs lede" style="left:310px;top:3079px;width:580px;text-align:center">Lorem ipsum dolor sit amet, consectetur adipiscing elit, sed do eiusmod tempor incididunt ut labore et dolore magna aliqua.</p>

<div class="blog-img" style="left:113px;background:radial-gradient(ellipse 110px 80px at 150px 90px,rgba(50,35,35,.6),rgba(0,0,0,0) 80%),linear-gradient(135deg,#a39497,#d2c3c4 50%,#8c7a7e)" role="img" aria-label="Instructor demonstrating brow work on a student"></div>
<div class="blog-img" style="left:448px;background:radial-gradient(ellipse 150px 50px at 150px 30px,rgba(212,170,60,.75),rgba(0,0,0,0) 80%),linear-gradient(180deg,#2f2a28 0%,#6a5a48 40%,#3a3230 75%,#bda58e 100%)" role="img" aria-label="Graduates holding certificates under gold and black balloons"></div>
<div class="blog-img" style="left:784px;background:radial-gradient(ellipse 120px 60px at 150px 130px,rgba(160,120,130,.5),rgba(0,0,0,0) 80%),linear-gradient(135deg,#e3dfde,#c9c1c2 55%,#a9a1a2)" role="img" aria-label="Students in white watching an in-person demonstration"></div>

<div class="blog-card active" style="left:136px"><p class="date">2 Jan, 2023</p><h5>Marela teaches personally</h5><div class="link">LEARN MORE</div></div>
<div class="blog-card" style="left:471px"><p class="date">5 Feb, 2023</p><h5>Graduate celebration</h5><div class="link">LEARN MORE</div></div>
<div class="blog-card" style="left:807px"><p class="date">10 July, 2023</p><h5>In personal demonstration</h5><div class="link">LEARN MORE</div></div>

<div class="arrow prev" style="left:31px;top:3225px"><svg width="14" height="14" viewBox="0 0 14 14"><path d="M9 2L4 7l5 5" stroke="#fff" stroke-width="2" fill="none"/></svg></div>
<div class="arrow next" style="left:1121px;top:3225px"><svg width="14" height="14" viewBox="0 0 14 14"><path d="M5 2l5 5-5 5" stroke="#fff" stroke-width="2" fill="none"/></svg></div>
<div class="btn btn-line" style="left:511px;top:3475px;width:178px;height:39px">View all</div>

<!-- newsletter -->
<section class="abs" role="img" aria-label="Rose band with a soft swirl pattern" style="left:0;top:3566px;width:1200px;height:270px;background:linear-gradient(180deg,#d9587a 0%,#d14d70 100%)"></section>
<h2 class="abs center serif" style="top:3606px;font-weight:400;font-size:46px;color:var(--white)">Subscribe Our Newsletter</h2>
<div class="abs" style="left:299px;top:3680px;width:602px;height:39px;background:rgba(255,255,255,.25);color:#fff;font-size:13px;padding:12px 18px">Your Email</div>
<div class="btn" style="left:511px;top:3752px;width:178px;height:37px;background:#fff;color:#333">Subscribe</div>

<!-- footer -->
<footer class="abs footer">
  <div class="abs serif" style="left:121px;top:42px;font-size:25px">Microblading</div>
  <div class="abs" role="img" aria-label="Map showing the salon location" style="left:121px;top:93px;width:196px;height:105px;background:linear-gradient(135deg,#eef1f2,#d6e2ea 60%,#c5d7e6)"></div>
  <p class="abs" style="left:121px;top:222px;font-size:10px;line-height:19px">Copyright © 2023 AtelierMarelaBrows.<br>All rights reserved.</p>

  <h6 style="left:432px">Quick Link</h6>
  <ul class="abs" style="left:432px;top:88px">
    <li>Home</li><li>About</li><li>Services</li><li>Academy</li><li>Testimonial</li><li>Contact Us</li>
  </ul>

  <h6 style="left:611px">Contact Us</h6>
  <div class="contact-row" style="left:611px;top:84px"><svg width="14" height="16" viewBox="0 0 14 16"><path d="M7 1a5 5 0 0 1 5 5c0 4-5 9-5 9S2 10 2 6a5 5 0 0 1 5-5z" fill="#d13f64"/><circle cx="7" cy="6" r="2" fill="#1a1a1a"/></svg>Atelier Marela Brows</div>
  <div class="contact-row" style="left:611px;top:116px">214 Alder Row, Brookhaven, NY 11520</div>
  <div class="contact-row" style="left:611px;top:146px"><span style="width:14px;height:14px;border-radius:50%;background:var(--rose)"></span>@marelabrows</div>
  <div class="contact-row" style="left:611px;top:177px"><span style="width:14px;height:14px;border-radius:50%;background:var(--rose)"></span>marelabrows</div>
  <div class="contact-row" style="left:611px;top:208px"><svg width="14" height="11" viewBox="0 0 14 11"><rect width="14" height="11" rx="1" fill="#d13f64"/><path d="M1 1l6 5 6-5" stroke="#fff" fill="none"/></svg>hello@ateliermarela.com</div>

  <h6 style="left:886px">Opening hours</h6>
  <p class="abs" style="left:886px;top:88px;font-size:10.5px">Monday to Sunday 11:00-18:00</p>
  <p class="abs" style="left:886px;top:120px;font-size:10.5px">We only take reservations, no walk in</p>
</footer>

</body>
</html>
```